Holiday Party Flyer Template

We are a company offering downloadable flyer designs to customers. We are seeking to broaden our design categories and would like to start with the party invitation category and in specific a Holiday themed party. There will be one winner but we will be following up with all designers who we feel have submitted quality work to discuss potentially licensing your designs so this could lead to much more work even if you dont win the contest. Please consider the following requirements and instructions:

* Holiday Party Flyer Design (Winter theme suitable for any small to large holdiay party event)

* Text elements to include: Event title, event location, event time and date, room for 2 to 3 paragraphs of text such as for attire, directions etc. Room for a company logo - note that the design should still look good if there is NOT a company logo since this may or may not be used by our client. Placeholder text can be used at the designers discretion in all areas described above. For example, you can feel free to call it "Winter Holiday Party" or "Annual Company Holiday Bash", etc. Its up to you - be creative.

* Design for letter size paper (8.5" by 11" 300dpi vector based!)

* If you only submit a single design, make sure the design does not contain anything specific to a certain religion (ie, Santa Claus, mangers and wise men or anything like that)

* Some of our clients may want to use the flyer design for Christmas or Hanukah themed events, so if you submit multiple designs, please feel free to include elements relating to these themes such as Santa and so on.

```html
<!DOCTYPE html>
<html lang="en">
<head>
<meta charset="utf-8">
<title>Midwinter Party Invitation</title>
<link rel="stylesheet" href="https://fonts.googleapis.com/css2?family=Source+Sans+3:ital,wght@0,400;0,700;1,400&family=Roboto+Condensed:wght@700&display=swap">
<style>
  :root {
    --red: #c4001a;
    --ice-dark: #3f7a73;
    --ice-mid: #6fa39d;
    --ice-light: #a9cccc;
    --snow: #d6e8ea;
    --white: #ffffff;
    --ink: #111111;
  }
  * { margin: 0; padding: 0; box-sizing: border-box; }
  html, body { width: 1200px; height: 928px; overflow: hidden; background: var(--snow); }
  .flyer {
    position: relative;
    width: 1200px;
    height: 928px;
    overflow: hidden;
    font-family: "Source Sans 3", "Myriad Pro", sans-serif;
    color: var(--red);
  }
  .scene {
    position: absolute;
    inset: 0;
    background:
      radial-gradient(ellipse 420px 260px at 1080px 300px, var(--ice-dark), transparent 70%),
      radial-gradient(ellipse 500px 200px at 300px 330px, rgba(63,122,115,0.55), transparent 70%),
      linear-gradient(to bottom, var(--ice-mid) 0%, #5e958f 28%, #86b4b0 40%, var(--ice-light) 46%, var(--snow) 54%, var(--snow) 100%);
  }
  .headline {
    position: absolute;
    left: 92px;
    top: 70px;
    font-weight: 700;
    font-size: 92px;
    line-height: 116px;
    letter-spacing: 1px;
    color: var(--red);
    text-shadow:
      0 0 0 var(--white),
      3px 0 0 var(--white), -3px 0 0 var(--white),
      0 3px 0 var(--white), 0 -3px 0 var(--white),
      2px 2px 0 var(--white), -2px -2px 0 var(--white),
      2px -2px 0 var(--white), -2px 2px 0 var(--white);
  }
  .logo-slot {
    position: absolute;
    left: 1017px;
    top: 73px;
    width: 127px;
    height: 100px;
    background: var(--red);
    padding: 14px 0 0 16px;
    font-family: "Roboto Condensed", sans-serif;
    font-weight: 700;
    font-size: 23px;
    line-height: 32px;
    color: var(--ink);
  }
  .invite {
    position: absolute;
    left: 126px;
    top: 478px;
  }
  .invite-lead { font-style: italic; font-size: 25px; line-height: 30px; }
  .invite-title { font-weight: 700; font-size: 31px; line-height: 40px; }
  .details {
    position: absolute;
    left: 126px;
    top: 578px;
    font-size: 19px;
    line-height: 22px;
  }
  .label { font-weight: 700; }
  .block + .block { margin-top: 22px; }
  .rsvp { margin-top: 6px; font-size: 15px; line-height: 20px; }
  .rsvp .label { font-size: 15px; }
  .notes {
    position: absolute;
    right: 70px;
    top: 603px;
    width: 312px;
    font-size: 19px;
    line-height: 22px;
    text-align: right;
  }
  .notes .justify { text-align: justify; text-align-last: right; }
  .notes .block + .block { margin-top: 21px; }
</style>
</head>
<body>
<main class="flyer">
  <div class="scene" role="img" aria-label="Teal-toned photograph of an icy landscape with two penguins facing each other on the snow"></div>

  <h1 class="headline">Come in out of<br>the cold!</h1>

  <div class="logo-slot">logo if<br>required</div>

  <section class="invite">
    <p class="invite-lead">You are warmly invited to our</p>
    <h2 class="invite-title">Midwinter Party</h2>
  </section>

  <section class="details">
    <div class="block">
      <p class="label">When</p>
      <p>Tuesday 21 December 2010</p>
      <p><span class="label">at</span> 7.30 pm</p>
    </div>
    <div class="block">
      <p class="label">Where</p>
      <p>Peter and Helen’s</p>
      <p>Our House</p>
      <p>Small Village</p>
      <p>Somewhere</p>
      <p>12345</p>
    </div>
    <div class="rsvp">
      <p class="label">RSVP</p>
      <p>Helen Marsh</p>
      <p>helen@ourmail.com</p>
    </div>
  </section>

  <section class="notes">
    <div class="block">
      <p class="label">Where to find us</p>
      <p class="justify">Leave the main road at exit 12. Take the next left down Happy Lane towards Small Village, first right on to Joy Avenue then second left. Our House is the third on the left.</p>
    </div>
    <div class="block">
      <p class="label">NB</p>
      <p>Wear something warm - mulled wine will be served under the stars!</p>
    </div>
  </section>
</main>
</body>
</html>
```